mobile app maker needs website redone

We currently have a running website that generates some traffic and looks ok but now we want to revamp it with professional modern eye catching design.
We are open to proposals and open to any new ideas or suggestions but we have to see your previous work.
our current site is www.drelvaapp.com

Industry/Entity Type

It Professional

Coding

Coded - Design and coding required

Number of Pages Required

5+ page

Font styles to use
Serif
Other font styles liked:
• open

Requirements
Must have
• modern look and feel easy to use
Nice to have
• responsive websites , example are as follow ,http://quorpa-layout.pagemint.site , vantri.com , http://saddex.pagemint.site

```html
<!DOCTYPE html>
<html lang="en">
<head>
<meta charset="utf-8">
<title>Drelva Marketing — Mobile Apps & Mobile Websites</title>
<link rel="stylesheet" href="https://fonts.googleapis.com/css2?family=Roboto:wght@300;400;500;700&display=swap">
<style>
:root{
  --orange:#f7a21b;
  --sky:#00b2e2;
  --navy:#0d3761;
  --heading:#173f6b;
  --green:#8cc63f;
  --cyan:#14b7e1;
  --ink:#222;
  --muted:#555;
  --white:#fff;
  --badge:#4a4a4a;
}
*{box-sizing:border-box;margin:0;padding:0}
html,body{width:1200px;height:2970px;overflow:hidden}
body{font-family:"Roboto",Arial,sans-serif;color:var(--ink);background:var(--white);position:relative}
.abs{position:absolute}

/* header */
.site-header{position:absolute;left:0;top:0;width:1200px;height:100px;background:rgba(255,255,255,.93);z-index:3}
.brand{position:absolute;left:143px;top:28px;display:flex;flex-direction:column;align-items:center}
.brand-mark{width:22px;height:22px;border-radius:50%;background:#111;margin-bottom:6px}
.brand-name{font-weight:700;font-size:17px;color:#111}
.main-nav a{position:absolute;top:42px;font-size:11px;font-weight:500;color:#111;text-decoration:none;white-space:nowrap}
.btn{position:absolute;top:35px;height:32px;border-radius:4px;color:#fff;font-size:11px;font-weight:500;display:flex;align-items:center;justify-content:center}
.btn-login{left:855px;width:97px;background:var(--green)}
.btn-preview{left:960px;width:121px;background:var(--cyan)}

/* hero */
.hero{position:absolute;left:0;top:0;width:1200px;height:657px;background:linear-gradient(120deg,#d9d9d9 0%,#b9b9b9 45%,#8f8f8f 70%,#c7c7c7 100%)}
.hero-box{position:absolute;left:145px;top:172px;width:334px;height:416px;background:rgba(0,0,0,.86);padding:40px 32px}
.hero-title{font-size:38px;line-height:36px;font-weight:400;color:#d9d9d9;text-transform:uppercase}
.hero-text{margin-top:22px;font-size:13px;line-height:25px;color:#aaa;font-weight:300}
.hero-more{display:inline-block;margin-top:24px;border:1px solid #ddd;color:#fff;font-size:13px;font-weight:500;padding:9px 12px}
.hero-arrow{position:absolute;top:350px;width:30px;height:50px}

/* welcome */
.welcome{position:absolute;left:0;top:657px;width:1200px;height:495px;background:var(--orange)}
.device-img{position:absolute;left:228px;top:18px;width:218px;height:450px;border-radius:34px;background:linear-gradient(180deg,#f2f2f2,#d7d7d7)}
.welcome-title{position:absolute;left:509px;top:112px;font-size:25px;font-weight:500;color:#fff}
.welcome-lead{position:absolute;left:509px;top:152px;font-size:14px;color:#fff;font-weight:300}
.welcome-body{position:absolute;left:509px;top:206px;width:548px;font-size:11px;line-height:20px;color:#fff;font-weight:300}
.welcome-body p+p{margin-top:14px}

/* features */
.features{position:absolute;left:0;top:1152px;width:1200px;height:495px;background:#fff}
.section-title{position:absolute;left:0;width:1200px;text-align:center;font-size:24px;font-weight:700;color:var(--heading);text-transform:uppercase}
.feature{position:absolute;width:285px}
.feature h3{display:flex;align-items:center;gap:10px;font-size:13px;font-weight:700;color:#111;text-transform:uppercase}
.feature h3 svg{flex:none}
.feature p{margin-top:30px;font-size:11px;line-height:20px;color:var(--muted)}
.dots{position:absolute;left:579px;top:1612px;display:flex;gap:7px}
.dots span{width:9px;height:9px;border-radius:50%;background:#ddd}
.dots span:first-child{background:var(--heading)}

/* showcase */
.showcase{position:absolute;left:0;top:1647px;width:1200px;height:759px;background:var(--sky)}
.showcase .section-title{top:66px;font-size:25px;font-weight:500}
.tile{position:absolute;width:311px;text-align:center}
.tile-img{height:184px}
.tile h4{margin-top:22px;font-size:13px;font-weight:500;color:var(--heading);text-transform:uppercase}
.tile p{margin-top:14px;font-size:11px;line-height:20px;color:#fff}

/* trust */
.trust{position:absolute;left:0;top:2406px;width:1200px;height:350px;background:#fff}
.trust h2{position:absolute;left:0;top:56px;width:1200px;text-align:center;font-size:23px;font-weight:700;color:var(--heading)}
.trust .sub{position:absolute;left:0;top:102px;width:1200px;text-align:center;font-size:13px;color:#222}
.platform{position:absolute;top:182px;width:100px;text-align:center;font-size:11px;color:#333}
.badge{display:block;width:64px;height:64px;margin:12px auto 24px;background:var(--badge);border-radius:6px}

/* footer */
.site-footer{position:absolute;left:0;top:2756px;width:1200px;height:214px;background:var(--navy);color:#fff}
.foot-brand{position:absolute;left:155px;top:42px;display:flex;flex-direction:column;align-items:center}
.foot-brand .brand-mark{background:#fff}
.foot-brand .brand-name{color:#fff}
.copyright{position:absolute;left:153px;top:110px;font-size:10px}
.foot-col{position:absolute;top:44px;list-style:none;font-size:10px;text-transform:uppercase}
.foot-col li{height:29px}
.social{position:absolute;left:723px;top:44px;font-size:10px;text-transform:uppercase}
.social-row{display:flex;gap:22px;margin-top:18px}
.social-row span{width:16px;height:16px;border-radius:50%;background:#fff}
</style>
</head>
<body>

<section class="hero">
  <div class="abs" role="img" aria-label="Photo of a hand holding a smartphone showing a welcome screen" style="left:0;top:0;width:1200px;height:657px"></div>
  <div class="hero-box">
    <h1 class="hero-title">Mobile apps &amp; mobile websites made easy!</h1>
    <p class="hero-text">DRELVAAPP.COM was built with small businesses in mind. Our goal is to help small businesses grow through affordable mobile marketing!</p>
    <span class="hero-more">LEARN MORE</span>
  </div>
  <svg class="hero-arrow" style="left:44px" viewBox="0 0 30 50"><polyline points="22,10 8,25 22,40" fill="none" stroke="#fff" stroke-width="5"/></svg>
  <svg class="hero-arrow" style="left:1128px" viewBox="0 0 30 50"><polyline points="8,10 22,25 8,40" fill="none" stroke="#fff" stroke-width="5"/></svg>
</section>

<header class="site-header">
  <div class="brand"><span class="brand-mark"></span><span class="brand-name">Drelva Marketing</span></div>
  <nav class="main-nav">
    <a style="left:457px">HOME</a><a style="left:517px">FEATURES</a><a style="left:610px">PRICING</a><a style="left:693px">CONTACT</a><a style="left:782px">SKIPPER</a>
  </nav>
  <span class="btn btn-login">LOGIN</span>
  <span class="btn btn-preview">PREVIEW YOUR APP</span>
</header>

<section class="welcome">
  <div class="device-img" role="img" aria-label="Smartphone displaying the Drelva Marketing app start screen"></div>
  <h2 class="welcome-title">WELCOME TO OUR DRELVA INC.</h2>
  <p class="welcome-lead">We provide the easiest way for businesses to create Mobile Apps!</p>
  <div class="welcome-body">
    <p>Consumers use their mobile devices to find the information they want, as soon as they want it. They depend on the instant accessibility of mobile apps to quickly tell them what they need to know, so they can make their purchasing decisions and get on with what they're doing.</p>
    <p>Smart business owners understand the power and importance of mobile marketing to their bottom line. They use mobile apps to connect with customers, share relevant news, offer great deals, increase foot traffic, take reservations, and boost their revenues. Whether they deliver a service, sell products in a store, or run a successful restaurant, they know that having a mobile app is one of the most effective ways to reach their customers, whether they're on the go or standing still.</p>
  </div>
</section>

<section class="features">
  <h2 class="section-title" style="top:62px">Customized app allows businesses to</h2>

  <div class="feature" style="left:145px;top:143px">
    <h3><svg width="20" height="20" viewBox="0 0 20 20"><circle cx="10" cy="6" r="5" fill="#8cc63f"/><path d="M1 20a9 8 0 0 1 18 0z" fill="#8cc63f"/></svg>Build customer loyalty</h3>
    <p>Make your customers feel special by offering discounts, coupons, and promotions just for using your app.</p>
  </div>
  <div class="feature" style="left:455px;top:143px">
    <h3><svg width="20" height="20" viewBox="0 0 20 20"><circle cx="10" cy="10" r="10" fill="#8cc63f"/><rect x="8.5" y="8" width="3" height="8" fill="#fff"/><circle cx="10" cy="5" r="1.8" fill="#fff"/></svg>Send push notifications</h3>
    <p>Deliver instant messages to your customers' mobile phones whenever you wish. While only 4% to 10% of emails get opened, push notifications get read 97% of the time.</p>
  </div>
  <div class="feature" style="left:766px;top:143px">
    <h3><svg width="22" height="20" viewBox="0 0 22 20"><ellipse cx="11" cy="8" rx="11" ry="8" fill="#8cc63f"/><path d="M4 13 L2 20 L10 15z" fill="#8cc63f"/></svg>Create viral buzz</h3>
    <p>Let customers quickly tell all of their friends about you using the built-in sharing capabilities of Frendly, Chirpo, Linkora, your blog, SMS, and Email.</p>
  </div>
  <div class="feature" style="left:145px;top:327px">
    <h3><svg width="24" height="18" viewBox="0 0 24 18"><path d="M0 18 L0 10 L6 4 L12 9 L18 2 L24 6 L24 18z" fill="#8cc63f"/></svg>Grow your list</h3>
    <p>Gather names and email addresses directly inside your app and easily export them into your favorite email marketing campaign service.</p>
  </div>
  <div class="feature" style="left:455px;top:327px">
    <h3><svg width="22" height="20" viewBox="0 0 22 20"><path d="M2 7 H7 L17 1 V19 L7 13 H2z" fill="#8cc63f"/><rect x="5" y="13" width="4" height="6" fill="#8cc63f"/></svg>Promote special events</h3>
    <p>Provide up-to-date information about all of your business events, sales, and promotions with an in-app events calendar that anyone can access.</p>
  </div>
  <div class="feature" style="left:766px;top:327px">
    <h3><svg width="20" height="20" viewBox="0 0 20 20"><rect x="1" y="10" width="3" height="9" fill="#8cc63f"/><rect x="6" y="5" width="3" height="14" fill="#8cc63f"/><rect x="11" y="8" width="3" height="11" fill="#8cc63f"/><rect x="16" y="2" width="3" height="17" fill="#8cc63f"/></svg>Gain more credibility</h3>
    <p>These are still the early years of the mobile app. Having one adds serious credibility to your business—especially among those who don't know how easy we make it.</p>
  </div>
</section>
<div class="dots"><span></span><span></span><span></span></div>

<section class="showcase">
  <h2 class="section-title">The #1 mobile app &amp; mobile website creator for small businesses</h2>

  <div class="tile" style="left:133px;top:111px">
    <div class="tile-img" role="img" aria-label="Hands browsing a shopping app on a phone" style="background:linear-gradient(135deg,#3a3a3a,#d8d2cc)"></div>
    <h4>Preview online</h4><p>We allow you to preview your apps as we build it</p>
  </div>
  <div class="tile" style="left:444px;top:111px">
    <div class="tile-img" role="img" aria-label="Hand holding a phone in a blurred store" style="background:linear-gradient(135deg,#9aa39b,#c9b89a)"></div>
    <h4>Incredibly easy</h4><p>Our easy to use content manage system allows<br>for beautiful app designs.</p>
  </div>
  <div class="tile" style="left:755px;top:111px">
    <div class="tile-img" role="img" aria-label="Person using a phone beside a laptop" style="background:linear-gradient(135deg,#e6e6e6,#9c9c9c)"></div>
    <h4>Powerful hosting</h4><p>Our servers are hosted in the cloud using<br>the latest hosting technology with 99.9% uptime for your apps.</p>
  </div>
  <div class="tile" style="left:133px;top:428px">
    <div class="tile-img" role="img" aria-label="Phone showing a recipe blog app" style="background:linear-gradient(135deg,#7b8a8c,#d9c6b4)"></div>
    <h4>Apps &amp; websitess</h4><p>We allow you to preview your apps as we build it</p>
  </div>
  <div class="tile" style="left:444px;top:428px">
    <div class="tile-img" role="img" aria-label="Phone with glowing app icons floating above it" style="background:linear-gradient(135deg,#0c2540,#2f7fc1)"></div>
    <h4>Customize everything</h4><p>Customize every pixel inside your mobile apps<br>within minutes using our pre-built designs or create your own.</p>
  </div>
  <div class="tile" style="left:755px;top:428px">
    <div class="tile-img" role="img" aria-label="Hand holding a phone against warm evening lights" style="background:linear-gradient(135deg,#2a2f55,#b7926a)"></div>
    <h4>Extremely affordable</h4><p>Is more affordable than a newspaper ad and shows a huge<br>return on investment for businesses.</p>
  </div>
</section>

<section class="trust">
  <h2>Small Businesses Trust DRELVA INC. Worldwide</h2>
  <p class="sub">DRELVA INC. is making mobile apps affordable and simple for small businesses.</p>
  <div class="platform" style="left:380px"><span class="badge"></span>Html 5</div>
  <div class="platform" style="left:564px"><span class="badge"></span>Pomelo</div>
  <div class="platform" style="left:762px"><span class="badge"></span>Botline</div>
</section>

<footer class="site-footer">
  <div class="foot-brand"><span class="brand-mark"></span><span class="brand-name">Drelva Marketing</span></div>
  <p class="copyright">Copyright 2016 drelvaapp.com</p>
  <ul class="foot-col" style="left:396px"><li>Home</li><li>Features</li><li>Pricing</li><li>Contact</li><li>Skipper</li></ul>
  <ul class="foot-col" style="left:543px"><li>Privacy Policy</li><li>Terms of Service</li></ul>
  <div class="social">Connect with us<div class="social-row"><span></span><span></span><span></span><span></span><span></span></div></div>
</footer>

</body>
</html>
```